Uplift: Covid 19 (Poster)

We are looking to create a 11 by 17 inch 1 page poster.
-- Please Include NKR’s logo
-- Use the colors and font and mimic the feel of from Steady Step, Steady Breath Resource - Dementia Risk Reduction Flyers - Northern Council for Tribal Longevity (nkrcircle.org)
--> https://nkrcircle.org/resource-dementia-risk-reduction-flyers/
Moto needs to be included and it is: Protect Your Community. Protect Your Elders. Stay Vaccinated.
Include funding statement at the bottom of document - small print:
This project is supported by the Bureau for Illness Monitoring and Response of the U.S. Office of Wellness and Family Programs (OWFP) as part of a financial assistance award totaling $20,007,444 with 100 percent funded by BIMR/OWFP. The contents are those of the author(s) and do not necessarily represent the official views of, nor an endorsement, by BIMR/OWFP, or the U.S. Government.

```html
<!DOCTYPE html>
<html lang="en">
<head>
<meta charset="utf-8">
<title>Uplift — Fight COVID-19 Poster</title>
<link href="https://fonts.googleapis.com/css2?family=Fira+Sans:wght@400;500;600;700;800&family=Roboto:wght@400&display=swap" rel="stylesheet">
<style>
  :root {
    --paper: #efe3cb;
    --paper-light: #f5ecd9;
    --edge: #c9d2b0;
    --brown: #6a3411;
    --logo-brown: #8a4a24;
    --red: #b3262a;
    --teal: #4ba4ae;
    --body-dark: #4a3a2c;
    --photo-violet: #8e3a8c;
    --photo-orange: #e58b3f;
  }
  * { margin: 0; padding: 0; box-sizing: border-box; }
  html, body { width: 776px; height: 1200px; overflow: hidden; }
  body { font-family: "Fira Sans", sans-serif; background: var(--paper); }

  .poster {
    position: relative;
    width: 776px; height: 1200px;
    background: radial-gradient(ellipse at 40% 45%, var(--paper-light) 0%, var(--paper) 70%);
    overflow: hidden;
  }
  .edge-band {
    position: absolute; top: 0; bottom: 0; width: 30px;
    background: linear-gradient(90deg, var(--edge), rgba(201,210,176,0));
    opacity: .7;
  }
  .edge-band--left { left: 0; }
  .edge-band--right { right: 0; transform: scaleX(-1); }

  .brand-uplift {
    position: absolute; left: 42px; top: 64px;
    font-weight: 800; font-size: 42px; letter-spacing: 3px;
    color: var(--logo-brown);
    display: flex; align-items: center; gap: 12px;
  }
  .brand-uplift .mark { width: 16px; height: 16px; background: var(--logo-brown); }

  .brand-nkr {
    position: absolute; left: 372px; top: 58px; width: 340px;
    display: flex; align-items: center; gap: 12px;
    font-weight: 600; font-size: 19px; line-height: 23px;
    color: var(--teal); text-transform: uppercase;
  }
  .brand-nkr .mark { flex: none; width: 36px; height: 36px; border-radius: 50%; background: var(--teal); }

  .motto {
    position: absolute; left: 36px; top: 176px;
    font-weight: 700; font-size: 33px; line-height: 41px; color: var(--brown);
    white-space: nowrap;
  }
  .headline {
    position: absolute; left: 34px; top: 272px;
    font-weight: 800; font-size: 70px; line-height: 80px;
    color: var(--red); letter-spacing: 3px; white-space: nowrap;
  }
  .intro {
    position: absolute; left: 36px; top: 378px;
    font-weight: 600; font-size: 20.5px; line-height: 28.5px; color: var(--brown);
    letter-spacing: .5px; white-space: nowrap;
  }
  .list {
    list-style: none; position: absolute; left: 50px;
    font-weight: 500; color: var(--red); white-space: nowrap;
  }
  .list li { position: relative; padding-left: 29px; }
  .list li::before {
    content: ""; position: absolute; left: 3px;
    width: 9px; height: 9px; background: var(--red); transform: rotate(45deg);
  }
  .facts { top: 500px; font-size: 19px; line-height: 23.5px; letter-spacing: .3px; }
  .facts li { margin-bottom: 9px; }
  .facts li::before { top: 8px; }
  .symptoms-intro {
    position: absolute; left: 42px; top: 664px;
    font-weight: 600; font-size: 20.5px; line-height: 28px; color: var(--brown);
    letter-spacing: .4px; white-space: nowrap;
  }
  .symptoms { top: 768px; font-size: 19.5px; line-height: 33px; letter-spacing: .3px; }
  .symptoms li::before { top: 12px; }

  .photo {
    position: absolute; left: 476px; top: 345px; width: 300px; height: 392px;
    border-radius: 260px 0 0 150px / 340px 0 0 150px;
    background:
      radial-gradient(ellipse at 70% 40%, var(--photo-violet) 0%, rgba(142,58,140,.6) 45%, rgba(142,58,140,0) 75%),
      radial-gradient(ellipse at 90% 85%, var(--photo-orange) 0%, rgba(229,139,63,0) 55%),
      radial-gradient(ellipse at 35% 80%, #7a2438 0%, rgba(122,36,56,0) 55%);
  }

  .funding {
    position: absolute; left: 34px; right: 34px; top: 1122px;
    font-family: "Roboto", sans-serif; font-size: 9.3px; line-height: 14.5px;
    color: var(--body-dark); text-align: center;
  }
</style>
</head>
<body>
<main class="poster">
  <div class="edge-band edge-band--left"></div>
  <div class="edge-band edge-band--right"></div>

  <div class="brand-uplift"><span>UPLIFT</span><span class="mark"></span></div>
  <div class="brand-nkr"><span class="mark"></span><span>Northern Council for Tribal Longevity</span></div>

  <h2 class="motto">Protect Your Community.<br>Protect Your Elders. Stay Vaccinated.</h2>
  <h1 class="headline">FIGHT COVID-19!</h1>

  <div class="photo" role="img" aria-label="Photograph of two Native elder women in traditional satin clothing with turquoise jewelry and a woven blanket"></div>

  <p class="intro">American Indian and Alaska Native people have<br>a higher risk of COVID-19 infection rate than<br>other population in the United States.</p>

  <ul class="list facts">
    <li>COVID-19 is a virus that spreads mainly<br>when infected people cough, sneeze, or talk.</li>
    <li>The best way to prevent yourself and others<br>from COVID-19 is by staying up to date with<br>vaccination boosters.</li>
  </ul>

  <p class="symptoms-intro">COVID-19 symptoms may take 2 to 14 days<br>to appear after exposure to the virus, and<br>symptoms may include:</p>

  <ul class="list symptoms">
    <li>Fever or chills</li>
    <li>Cough</li>
    <li>Shortness of breath or difficulty breathing</li>
    <li>Fatigue</li>
    <li>Muscle or body aches</li>
    <li>Headache</li>
    <li>New loss of taste or smell</li>
    <li>Sore throat</li>
    <li>Congestion or runny nose</li>
  </ul>

  <p class="funding">This project is supported by the Bureau for Illness Monitoring and Response of the U.S. Office of Wellness and Family Programs (OWFP) as part of a financial assistance award totaling $20,007,444 with 100 percent funded by BIMR/OWFP. The contents are those of the author(s) and do not necessarily represent the official views of, nor an endorsement, by BIMR/OWFP, or the U.S. Government</p>
</main>
</body>
</html>
```